UI Graphics Design For Web Based Home Control

Hi,
Our company Kelvo Systems is looking for user interface graphics in form of *.psd for home control user interface for a real system which can be used on mobile and PC/MAC.
In Ideal solution, the same interface should be used on mobile, tablets, computers. It changes only to fit the size of the screen. The bigger the screen, the more options you have visible on same view. The user should get familiar interface logic with every device.
The design should have at least the following views covered:
1. Lights view
- List of rooms and lamps
- You can see the status and you can switch it on/off
2. Login view
- Logo (company logo attached)
- Username field
- Password field
3. Dashboard view
- Indicating and choosing home/not home
- Can go to lights view
- Can go to settings view
- Notification list
4. Settings view
- View and edit users
- View and edit lights
Show us your view of ideal home control UI :)
Updates
Time of the project extended by 10 days to receive more designs. If someone sees that the reward should be increased, please also provide the amount expected with the first design. We are willing to increase the amount paid if we see a good design.
Reason: We expect to receive more designs. We are willing to increase the reward if we see good and acceptable designs. Please provide the amount expected with the first design. Project will end with full designs available.
We added our input as an attachment how we see the UI logic. Please have a look into the file.
Reason: We are seeing some good designs. We increased the budget. We are still not where we expect.
Industry/Entity Type
It Company
Look and feel
Each slider illustrates characteristics of the customer's brand and the style your logo design should communicate.

```html
<!DOCTYPE html>
<html lang="en">
<head>
<meta charset="utf-8">
<title>Kelvo Systems – Home Control Dashboard</title>
<link href="https://fonts.googleapis.com/css2?family=Nunito+Sans:wght@400;600;700&display=swap" rel="stylesheet">
<style>
  :root {
    --frame-blue: #0b3b8c;
    --panel-green: #0a9a46;
    --panel-teal: #0b6a5e;
    --panel-navy: #0b3a7a;
    --dark-panel: rgba(20, 28, 30, 0.72);
    --card-blue: #173f8a;
    --card-edge: #2a5bb0;
    --label-lime: #b4e21e;
    --value-white: #ffffff;
    --button-dark: #1c1f22;
    --button-light: #3a3e42;
    --toggle-navy: #14336e;
    --toggle-green: #22b23a;
    --notice-green: #16a23a;
    --notice-text: #0e2a12;
    --warn-yellow: #f2e64a;
    --icon-grey: #c8ccd2;
  }
  * { box-sizing: border-box; margin: 0; padding: 0; }
  html, body {
    width: 1200px; height: 990px; overflow: hidden;
    background: var(--frame-blue);
    font-family: "Nunito Sans", sans-serif;
  }
  .screen {
    position: relative; width: 1200px; height: 990px;
    background: var(--frame-blue);
  }
  .stage {
    position: absolute; left: 17px; top: 22px; width: 1166px; height: 948px;
    border-radius: 16px; overflow: hidden;
    background: linear-gradient(180deg, #0d3d2e 0%, #0c2a26 55%, #0a1f3c 100%);
  }
  .stage-art {
    position: absolute; inset: 0;
    background: radial-gradient(circle at 62% 78%, #1b3c7a 0%, #13294e 22%, transparent 45%),
                radial-gradient(circle at 70% 20%, #1d4a33 0%, transparent 50%);
  }
  .sidebar {
    position: absolute; left: 0; top: 0; width: 440px; height: 100%;
    background: linear-gradient(170deg, var(--panel-green) 0%, var(--panel-teal) 45%, var(--panel-navy) 100%);
  }
  .brand {
    position: absolute; left: 69px; top: 104px; width: 300px;
    font-weight: 700; font-size: 34px; line-height: 1; color: var(--value-white);
    display: flex; align-items: center; gap: 12px; white-space: nowrap;
  }
  .brand-dot { flex: none; width: 18px; height: 18px; border-radius: 50%; background: var(--value-white); }
  .presence {
    position: absolute; left: 39px; top: 204px; width: 323px; height: 54px;
    display: flex; border-radius: 8px; overflow: hidden;
    box-shadow: 0 2px 4px rgba(0,0,0,.35);
  }
  .presence-option {
    display: flex; align-items: center; gap: 12px; padding-left: 28px;
    color: var(--value-white); font-size: 21px; font-weight: 600;
  }
  .presence-home { width: 162px; background: var(--toggle-navy); }
  .presence-away { flex: 1; background: var(--toggle-green); padding-left: 14px; }
  .nav-button { position: absolute; left: 39px; display: flex; align-items: center; }
  .nav-icon {
    width: 80px; height: 80px; border-radius: 50%;
    background: radial-gradient(circle, #1a4a6a 0%, #123350 100%);
    display: flex; align-items: center; justify-content: center;
    position: relative; z-index: 1;
  }
  .nav-icon-core {
    width: 48px; height: 48px; border-radius: 50%; background: #2fb52f;
    display: flex; align-items: center; justify-content: center;
  }
  .nav-label {
    margin-left: -16px; width: 260px; height: 52px; border-radius: 0 8px 8px 0;
    background: linear-gradient(180deg, var(--button-light) 0%, var(--button-dark) 55%);
    color: var(--value-white); font-size: 28px; font-weight: 600;
    display: flex; align-items: center; justify-content: center;
    box-shadow: 0 3px 5px rgba(0,0,0,.4);
  }
  .nav-lights { top: 300px; }
  .nav-settings { top: 390px; }
  .notice {
    position: absolute; left: 28px; top: 809px; width: 364px; height: 107px;
    border-radius: 6px; background: #13406a; padding: 5px;
  }
  .notice-body {
    width: 100%; height: 100%; border-radius: 4px; background: var(--notice-green);
    display: flex; align-items: center; gap: 30px; padding-left: 24px;
    color: var(--notice-text); font-size: 20px; line-height: 1.3;
  }
  .content {
    position: absolute; left: 413px; top: 26px; width: 734px; height: 893px;
    background: var(--dark-panel); border-radius: 6px;
  }
  .section-title {
    position: absolute; left: 62px; display: flex; align-items: center; gap: 18px;
    color: var(--value-white); font-size: 32px; font-weight: 400;
  }
  .title-lights { top: 52px; }
  .title-sensors { top: 411px; }
  .card {
    position: absolute; left: 42px; width: 660px; border-radius: 10px;
    background: var(--card-blue); border-top: 1px solid var(--card-edge);
    box-shadow: 0 3px 6px rgba(0,0,0,.4);
  }
  .card-lights { top: 137px; height: 228px; }
  .card-sensors { top: 487px; height: 228px; }
  .row {
    position: absolute; left: 26px; right: 0; height: 40px;
    display: flex; align-items: center; font-size: 27px;
  }
  .row-icon { width: 30px; display: flex; justify-content: center; margin-right: 18px; }
  .row-label { color: var(--label-lime); width: 430px; }
  .row-value { color: var(--value-white); }
  .switch {
    width: 106px; height: 38px; border-radius: 19px; background: #f4f5f6;
    display: flex; align-items: center; position: relative;
    box-shadow: inset 0 1px 3px rgba(0,0,0,.3);
  }
  .switch-knob {
    width: 36px; height: 36px; border-radius: 50%; background: #fff;
    box-shadow: 0 1px 3px rgba(0,0,0,.45); margin-left: 1px;
  }
  .switch-text { position: absolute; right: 16px; color: #7d8590; font-size: 22px; font-weight: 700; }
</style>
</head>
<body>
<div class="screen">
  <div class="stage">
    <div class="stage-art" role="img" aria-label="Dark green and blue textured backdrop with a large circular machine motif"></div>

    <aside class="sidebar">
      <div class="brand"><span class="brand-dot"></span>Kelvo Systems</div>

      <div class="presence">
        <div class="presence-option presence-home">
          <svg width="24" height="22" viewBox="0 0 24 22"><path d="M12 1 L23 11 H19 V21 H14 V14 H10 V21 H5 V11 H1 Z" fill="#fff"/></svg>
          Home
        </div>
        <div class="presence-option presence-away">
          <svg width="22" height="22" viewBox="0 0 22 22"><rect x="1.5" y="1.5" width="19" height="19" fill="none" stroke="#fff" stroke-width="2"/><path d="M6 16 L16 6 M11 6 H16 V11 M6 11 V16 H11" fill="none" stroke="#fff" stroke-width="2"/></svg>
          Not Home
        </div>
      </div>

      <div class="nav-button nav-lights">
        <div class="nav-icon"><div class="nav-icon-core">
          <svg width="20" height="28" viewBox="0 0 20 28"><path d="M10 2 A8 8 0 0 1 15 16 V20 H5 V16 A8 8 0 0 1 10 2 Z" fill="none" stroke="#fff" stroke-width="2"/><path d="M6 23 H14 M7 26 H13" stroke="#fff" stroke-width="2"/></svg>
        </div></div>
        <div class="nav-label">Lights View</div>
      </div>

      <div class="nav-button nav-settings">
        <div class="nav-icon"><div class="nav-icon-core">
          <svg width="28" height="28" viewBox="0 0 28 28"><circle cx="14" cy="14" r="8" fill="none" stroke="#fff" stroke-width="5" stroke-dasharray="4 2.3"/><circle cx="14" cy="14" r="4" fill="#fff"/></svg>
        </div></div>
        <div class="nav-label">Settings View</div>
      </div>

      <div class="notice"><div class="notice-body">
        <svg width="50" height="44" viewBox="0 0 50 44"><path d="M25 2 L48 42 H2 Z" fill="var(--warn-yellow)" stroke="#3a3a10" stroke-width="2" stroke-linejoin="round"/><rect x="23" y="15" width="4" height="15" fill="#1a1a1a"/><rect x="23" y="33" width="4" height="4" fill="#1a1a1a"/></svg>
        <p>Turn off the lights<br>sharp at 6: AM</p>
      </div></div>
    </aside>

    <main class="content">
      <h2 class="section-title title-lights">
        <svg width="22" height="34" viewBox="0 0 22 34"><path d="M11 2 A9 9 0 0 1 16 19 V24 H6 V19 A9 9 0 0 1 11 2 Z" fill="none" stroke="var(--icon-grey)" stroke-width="2"/><path d="M7 27 H15 M8 31 H14" stroke="var(--icon-grey)" stroke-width="2"/></svg>
        Lights
      </h2>
      <section class="card card-lights">
        <div class="row" style="top:28px">
          <span class="row-icon"><svg width="12" height="30" viewBox="0 0 12 30"><rect x="3" y="1" width="6" height="20" rx="3" fill="var(--icon-grey)"/><circle cx="6" cy="24" r="5" fill="var(--icon-grey)"/></svg></span>
          <span class="row-label">Home Temp</span><span class="row-value">19.9 °C</span>
        </div>
        <div class="row" style="top:94px">
          <span class="row-icon"><svg width="26" height="26" viewBox="0 0 26 26"><circle cx="13" cy="13" r="5" fill="var(--icon-grey)"/><path d="M13 1 V6 M13 20 V25 M1 13 H6 M20 13 H25 M4.5 4.5 L8 8 M18 18 L21.5 21.5 M4.5 21.5 L8 18 M18 8 L21.5 4.5" stroke="var(--icon-grey)" stroke-width="2"/></svg></span>
          <span class="row-label">Home Humidity</span><span class="row-value">58%</span>
        </div>
        <div class="row" style="top:161px">
          <span class="row-icon"><svg width="18" height="28" viewBox="0 0 18 28"><path d="M9 2 A7 7 0 0 1 13 15 V19 H5 V15 A7 7 0 0 1 9 2 Z" fill="none" stroke="var(--icon-grey)" stroke-width="2"/><path d="M5 22 H13 M6 25 H12" stroke="var(--icon-grey)" stroke-width="2"/></svg></span>
          <span class="row-label">Light 14 &nbsp;Home</span>
          <span class="switch" aria-label="Light 14 switch, off"><span class="switch-knob"></span><span class="switch-text">OFF</span></span>
        </div>
      </section>

      <h2 class="section-title title-sensors">
        <svg width="30" height="30" viewBox="0 0 30 30"><circle cx="15" cy="15" r="13" fill="none" stroke="var(--icon-grey)" stroke-width="2"/><circle cx="15" cy="15" r="7" fill="none" stroke="var(--icon-grey)" stroke-width="2"/><path d="M15 15 L25 6" stroke="var(--icon-grey)" stroke-width="2"/><circle cx="15" cy="15" r="2" fill="var(--icon-grey)"/></svg>
        Sensors
      </h2>
      <section class="card card-sensors">
        <div class="row" style="top:40px">
          <span class="row-icon"><svg width="12" height="30" viewBox="0 0 12 30"><rect x="3" y="1" width="6" height="20" rx="3" fill="var(--icon-grey)"/><circle cx="6" cy="24" r="5" fill="var(--icon-grey)"/></svg></span>
          <span class="row-label">Bathroom Temp</span><span class="row-value">20.3 °C</span>
        </div>
        <div class="row" style="top:106px">
          <span class="row-icon"><svg width="12" height="30" viewBox="0 0 12 30"><rect x="3" y="1" width="6" height="20" rx="3" fill="var(--icon-grey)"/><circle cx="6" cy="24" r="5" fill="var(--icon-grey)"/></svg></span>
          <span class="row-label">Bathroom Humidity</span><span class="row-value">61%</span>
        </div>
      </section>
    </main>
  </div>
</div>
</body>
</html>
```